Hvac service truck vinyl decals

2023 k270 LDR
You can find the logo i want to use at
maplerockac.com
Include
Logo
Keep Calm, Ring Maple!
Website
Ph# 5047319086

```html
<!DOCTYPE html>
<html lang="en">
<head>
<meta charset="utf-8">
<title>Maple Rock AC – Truck Side Decal</title>
<link rel="stylesheet" href="https://fonts.googleapis.com/css2?family=Bebas+Neue&display=swap">
<style>
  :root{
    --page:#ffffff;
    --panel-light:#f4f4f5;
    --panel-mid:#dcdcde;
    --blue-deep:#0a5f9e;
    --blue-main:#1490d2;
    --blue-cyan:#00c6f4;
    --brand-blue:#3a9edc;
    --alert-red:#f0141c;
    --white:#ffffff;
  }
  html,body{margin:0;padding:0;}
  body{
    width:1200px;height:1065px;overflow:hidden;
    background:var(--page);
    display:flex;align-items:center;justify-content:center;
  }
  .decal-layout{width:1120px;height:360px;display:block;}
  .decal-text{font-family:"Bebas Neue",sans-serif;}
  .brand-name{fill:var(--brand-blue);font-size:124px;letter-spacing:2px;}
  .tagline{fill:var(--white);font-size:44px;letter-spacing:0.5px;}
  .phone{fill:var(--alert-red);stroke:var(--white);stroke-width:3px;paint-order:stroke;font-size:74px;}
</style>
</head>
<body>
<svg class="decal-layout" viewBox="0 0 1765 567" xmlns="http://www.w3.org/2000/svg" aria-label="Maple Rock AC truck side decal layout">
  <defs>
    <linearGradient id="panelShade" x1="0" y1="0" x2="0" y2="1">
      <stop offset="0" stop-color="var(--panel-mid)"/>
      <stop offset="0.3" stop-color="var(--panel-light)"/>
      <stop offset="0.75" stop-color="var(--panel-light)"/>
      <stop offset="1" stop-color="var(--panel-mid)"/>
    </linearGradient>
    <linearGradient id="wrapBlue" x1="0" y1="0" x2="1" y2="1">
      <stop offset="0" stop-color="var(--blue-main)"/>
      <stop offset="0.6" stop-color="var(--blue-main)"/>
      <stop offset="1" stop-color="var(--blue-deep)"/>
    </linearGradient>
    <linearGradient id="waveCyan" x1="0" y1="0" x2="1" y2="0">
      <stop offset="0" stop-color="var(--blue-cyan)"/>
      <stop offset="1" stop-color="#22b4ea"/>
    </linearGradient>
    <clipPath id="wrapShape">
      <path d="M38 392 C400 386 800 376 973 368 L973 107 L1720 102 L1718 240 C1695 250 1660 262 1650 290 C1680 302 1700 306 1716 306 L1716 335 L1690 350 L1680 480 L1465 565 C1460 400 1380 240 1275 240 C1160 240 1080 340 1065 450 L38 450 Z"/>
    </clipPath>
  </defs>

  <rect class="panel-backdrop" width="1765" height="567" fill="url(#panelShade)"/>

  <g class="side-wrap" clip-path="url(#wrapShape)">
    <rect width="1765" height="567" fill="url(#wrapBlue)"/>
    <path class="cool-wave" fill="url(#waveCyan)"
      d="M0 394 C700 382 1200 330 1420 250 C1560 200 1660 150 1765 112 L1765 240 C1600 310 1350 425 1000 452 L0 452 Z"/>
  </g>

  <g class="brand-lockup">
    <circle cx="196" cy="258" r="52" fill="var(--brand-blue)"/>
    <text class="decal-text brand-name" x="272" y="304">MAPLE ROCK AC</text>
  </g>

  <g class="call-to-action" text-anchor="middle">
    <text class="decal-text tagline" x="1288" y="160">KEEP CALM RING MAPLE</text>
    <text class="decal-text phone" x="1288" y="226">504 7 319 086</text>
  </g>
</svg>
</body>
</html>
```